High End Notary Service Business Card Design

Want a professional and elegant/luxurious business card that is clean and simple in the design. A notary is a trusted professional that helps people sign very important documents. The card should be in alignment with this service provided.

Most of the time, service will be for the purchase of a home or refinance of a mortgage

There is NO LOGO. This is aesthetic. A look and feel. Conveying professionalism and concierge level of service.

Target Market(s)

Other business professionals, Lawyers, Escrow Officers, Loan Officers

Industry/Entity Type

Legal

Contact Information for Business Card

This will be a one-sided business card

Colors
35a7d7
3176b5
85cae6
d3a5cc
b868aa
ffffff
0356a4

Requirements
Must have
• Lorena T. Mirabel-Hodgkins
Notary Public

642-871-3094
MirabelSigningDesk@Wexmail.com
Nice to have
• Headshot photo below. Convey the aspect of signing documents. No black cards. Preference is shades of blue: light blue, navy, aqua, gold, white, or lavendar, etc.
Should not have
• No scales or legal scales.

```html
<!DOCTYPE html>
<html lang="en">
<head>
<meta charset="utf-8">
<title>Lorena T. Mirabel-Hodgkins — Notary Public</title>
<link href="https://fonts.googleapis.com/css2?family=Montserrat:wght@400;700&display=swap" rel="stylesheet">
<style>
  :root {
    --backdrop: #e9e9e9;
    --card: #ffffff;
    --ink: #2e2e2e;
    --ink-soft: #3a3a3a;
    --aqua: #35a7d7;
    --mid-blue: #348fc8;
    --deep-blue: #3176b5;
  }
  html, body {
    margin: 0;
    width: 1200px;
    height: 800px;
    overflow: hidden;
    background: var(--backdrop);
  }
  .business-card {
    position: absolute;
    left: 75px;
    top: 100px;
    width: 1050px;
    height: 600px;
    background: var(--card);
    box-shadow: 0 6px 24px rgba(0,0,0,0.12);
    overflow: hidden;
    font-family: "Montserrat", sans-serif;
    color: var(--ink);
  }
  .corner-accent {
    position: absolute;
    right: 0;
    bottom: 0;
    width: 1050px;
    height: 600px;
  }
  .identity {
    position: absolute;
    left: 0;
    right: 60px;
    top: 150px;
    display: flex;
    flex-direction: column;
    align-items: center;
    text-align: center;
  }
  .person-name {
    margin: 0;
    font-weight: 700;
    font-size: 50px;
    letter-spacing: 0.5px;
  }
  .person-title {
    margin: 6px 0 0 120px;
    font-weight: 400;
    font-size: 32px;
    letter-spacing: 1.5px;
    color: var(--ink-soft);
  }
  .divider {
    margin: 28px 0 26px 60px;
    width: 200px;
    height: 8px;
  }
  .contact-line {
    margin: 0;
    font-weight: 400;
    font-size: 34px;
    letter-spacing: 1.5px;
    line-height: 1.35;
    color: var(--ink-soft);
  }
</style>
</head>
<body>
  <div class="business-card">
    <svg class="corner-accent" viewBox="0 0 1050 600" aria-hidden="true">
      <polygon points="1050,250 1050,600 745,600" fill="var(--aqua)"/>
      <polygon points="1050,340 1050,600 822,600" fill="var(--mid-blue)"/>
      <polygon points="1050,430 1050,600 900,600" fill="var(--deep-blue)"/>
    </svg>

    <div class="identity">
      <h1 class="person-name">Lorena T. Mirabel-Hodgkins</h1>
      <p class="person-title">Notary Public</p>
      <svg class="divider" viewBox="0 0 200 8" aria-hidden="true">
        <path d="M0,6 Q100,-1 200,1 Q100,3 0,6 Z" fill="var(--ink)"/>
      </svg>
      <p class="contact-line">642-871-3094</p>
      <p class="contact-line">MirabelSigningDesk@Wexmail.com</p>
    </div>
  </div>
</body>
</html>
```